Steel Rebar Fabrication Company needs Facebook Ads & page, Instagram Ads & pages designed.

I want to put out an Instagram, Facebook ad, and LinkedIn campaign out for my new company, Ridgeform Metals Inc. I want the ads to be short but clean, clear and precise. I want our address: 4817 Alderbrook Cres. Tsawwassen, BC. I want our hours of operation to be listed 8:00am to 4:00pm Monday to Friday. Product Delivery to your job site or pick up at our yard available. We can cut, bend to custom and standard shapes based upon Canadian NRQ Standards. We offer products ranging from 10mm to 35mm diameter Grade 400W rebar. We can bend stirrups, dowels, hairpins; whatever your company needs to complete your product. Whether it is a small project, Tilt Up warehouse, Wood Frame Construction with Concrete parkade foundation; we have the team to meet your needs.
Email address: info@ridgeformmetalsinc.ca
We can service all areas of British Columbia.

Target Market(s)

Construction Company's for homes, condominiums, warehouses, commercial, industrial, and infrastructure projects. As well, as the every day DIY home improvement or renovator.

Industry/Entity Type

Construction

Requirements
Nice to have
• Would like to see a image of the rebar steel that I have provided in the ad. Even if it is in the background with a lower opacity level. Bonus if someone includes any of the movie files I have uploaded.

```html
<!DOCTYPE html>
<html lang="en">
<head>
<meta charset="utf-8">
<title>Ridgeform Metals Inc. – Rebar Fabrication Ad</title>
<link rel="stylesheet" href="https://fonts.googleapis.com/css2?family=Source+Sans+3:wght@400;600;700&display=swap">
<style>
  :root {
    --ink: #231f20;
    --brand-red: #be1e2d;
    --panel-red: rgba(190, 30, 45, 0.72);
    --white: #ffffff;
    --sky-warm: #f9c796;
    --sky-blush: #f2d5c9;
    --sky-cool: #8e9ea5;
    --steel-dark: #3c4a52;
  }
  * { box-sizing: border-box; margin: 0; padding: 0; }
  html, body {
    width: 1200px;
    height: 628px;
    overflow: hidden;
    background: var(--white);
  }
  .ad {
    position: relative;
    width: 1200px;
    height: 628px;
    overflow: hidden;
    font-family: "Source Sans 3", "Myriad Pro", sans-serif;
    color: var(--ink);
  }
  .ad__backdrop {
    position: absolute;
    inset: 0;
    background:
      linear-gradient(200deg, rgba(60, 74, 82, 0.55) 0%, rgba(60, 74, 82, 0) 38%),
      linear-gradient(100deg, var(--sky-warm) 0%, var(--sky-blush) 45%, #d9c2bd 65%, var(--sky-cool) 100%);
  }
  .ad__crane-photo {
    position: absolute;
    right: 0;
    top: 0;
    width: 520px;
    height: 628px;
    background: linear-gradient(160deg, rgba(60, 74, 82, 0.15) 0%, rgba(60, 74, 82, 0.45) 55%, rgba(90, 50, 45, 0.55) 100%);
  }
  .offer {
    position: absolute;
    left: 108px;
    top: 70px;
    width: 570px;
  }
  .offer__delivery {
    font-size: 19.5px;
    font-weight: 600;
    letter-spacing: -0.2px;
    line-height: 1;
    text-align: center;
  }
  .offer__headline {
    margin-top: 43px;
    font-size: 43px;
    font-weight: 700;
    line-height: 44px;
    letter-spacing: -0.3px;
    text-align: center;
  }
  .offer__headline .accent { color: var(--brand-red); }
  .offer__details {
    margin-top: 30px;
    font-size: 16.6px;
    font-weight: 600;
    line-height: 21px;
    text-align: justify;
    text-align-last: left;
  }
  .offer__coverage {
    margin-top: 30px;
    font-size: 20px;
    font-weight: 600;
    color: var(--brand-red);
    text-align: center;
  }
  .signoff {
    position: absolute;
    left: 108px;
    top: 507px;
    width: 570px;
    border-top: 2px solid var(--ink);
    text-align: center;
  }
  .signoff__name {
    display: inline-block;
    margin-top: 34px;
    font-size: 28px;
    font-weight: 700;
    color: var(--ink);
    letter-spacing: 0.5px;
  }
  .contact-panel {
    position: absolute;
    left: 836px;
    top: 150px;
    width: 274px;
    height: 328px;
    background: var(--panel-red);
    color: var(--white);
    font-weight: 700;
  }
  .contact-panel__row {
    position: absolute;
    left: 27px;
    right: 10px;
    display: flex;
    line-height: 24px;
  }
  .contact-panel__label { width: 27px; flex: none; }
  .contact-panel__address { top: 52px; font-size: 19.5px; }
  .contact-panel__email { top: 124px; font-size: 16px; }
  .contact-panel__rule {
    position: absolute;
    left: 34px;
    width: 212px;
    top: 202px;
    border-top: 2px solid var(--white);
  }
  .contact-panel__hours {
    position: absolute;
    left: 0;
    right: 0;
    top: 220px;
    text-align: center;
    font-size: 20px;
    line-height: 24px;
  }
</style>
</head>
<body>
<main class="ad">
  <div class="ad__backdrop" role="img" aria-label="Low-angle photograph of a construction tower crane against a warm hazy sky"></div>
  <div class="ad__crane-photo" role="img" aria-label="Tower crane mast and building framework rising on the right"></div>

  <section class="offer">
    <p class="offer__delivery">Product delivery to your job site or pick up at our yard available!</p>
    <h1 class="offer__headline">
      We can <span class="accent">CUT</span>, <span class="accent">BEND</span> to<br>
      <span class="accent">CUSTOM</span> &amp; <span class="accent">STANDARD SHAPES</span><br>
      based upon Canadian<br>
      NRQ Standards
    </h1>
    <p class="offer__details">We offer products ranging from 10mm to 35mm diameter Grade 400W rebar. We can bend stirrups, dowels, hairpins; whatever your company needs to complete your product. Whether it is a small project, Tilt Up warehouse, Wood Frame Construction with Concrete parkade foundation; we have the team to meet your needs.</p>
    <p class="offer__coverage">We can service all areas of British Columbia.</p>
  </section>

  <footer class="signoff">
    <span class="signoff__name">Ridgeform Metals Inc.</span>
  </footer>

  <aside class="contact-panel">
    <div class="contact-panel__row contact-panel__address">
      <span class="contact-panel__label">a :</span>
      <span>4817 Alderbrook Cres.<br>Tsawwassen, BC</span>
    </div>
    <div class="contact-panel__row contact-panel__email">
      <span class="contact-panel__label">e :</span>
      <span>info@ridgeformmetalsinc.ca</span>
    </div>
    <div class="contact-panel__rule"></div>
    <p class="contact-panel__hours">8:00am - 4:00pm<br>Monday to Friday</p>
  </aside>
</main>
</body>
</html>
```